Painting Company Business Card

Brightwell Painting needs a new business card. See attachments for our logo and current card as an example.
We want to utilize the same colors in the logo, and keep all the information that is currently on it. Just need an updated and modern design.
We are open to loosing the Association Logos if it means a better design.
We are also entertaining a spot for a picture of a headshot of the person listed on the card. Head shot can be finished later.

```html
<!DOCTYPE html>
<html lang="en">
<head>
<meta charset="UTF-8">
<title>Brightwell Painting — Business Card</title>
<link href="https://fonts.googleapis.com/css2?family=Work+Sans:wght@400;500;700&display=swap" rel="stylesheet">
<style>
  :root {
    --brand-green: #3a4129;
    --card-white: #ffffff;
    --ink: #2b2b2b;
    --ink-soft: #555555;
    --stage: #e6e6e3;
    --logo-light: #e9ebe4;
  }
  * { box-sizing: border-box; margin: 0; padding: 0; }
  html, body {
    width: 1200px;
    height: 900px;
    overflow: hidden;
    background: var(--stage);
    font-family: "Work Sans", sans-serif;
  }
  .canvas {
    position: relative;
    width: 1200px;
    height: 900px;
  }
  .card {
    position: absolute;
    left: 285px;
    width: 630px;
    height: 360px;
    border-radius: 4px;
    box-shadow: 0 10px 28px rgba(0,0,0,0.18);
  }
  .card-front {
    top: 70px;
    background: var(--card-white);
    display: flex;
    align-items: center;
  }
  .card-back {
    top: 470px;
    background: var(--brand-green);
    display: flex;
    align-items: center;
    justify-content: center;
  }
  .front-brand {
    width: 300px;
    padding-left: 48px;
  }
  .brand-name {
    color: var(--brand-green);
    font-weight: 700;
    font-size: 38px;
    line-height: 1.05;
    letter-spacing: -0.5px;
  }
  .brand-mark {
    display: inline-block;
    width: 14px;
    height: 14px;
    background: var(--brand-green);
    margin-bottom: 14px;
  }
  .divider {
    width: 2px;
    height: 210px;
    background: var(--brand-green);
    margin: 0 34px 0 0;
  }
  .contact {
    color: var(--ink);
  }
  .person-name {
    font-weight: 500;
    font-size: 21px;
    letter-spacing: 1.5px;
    text-transform: uppercase;
    color: var(--ink);
  }
  .person-role {
    font-size: 13px;
    color: var(--ink-soft);
    margin-bottom: 12px;
  }
  .address {
    font-size: 14px;
    line-height: 1.4;
    margin-bottom: 8px;
  }
  .contact-line {
    display: flex;
    align-items: center;
    gap: 8px;
    font-size: 14px;
    line-height: 1.55;
  }
  .contact-line svg {
    width: 11px;
    height: 11px;
    flex: none;
  }
  .back-brand {
    color: var(--logo-light);
    font-weight: 700;
    font-size: 52px;
    letter-spacing: -0.5px;
    display: flex;
    align-items: center;
    gap: 18px;
  }
  .back-mark {
    width: 18px;
    height: 18px;
    background: var(--logo-light);
  }
</style>
</head>
<body>
<main class="canvas">
  <section class="card card-front">
    <div class="front-brand">
      <span class="brand-mark"></span>
      <div class="brand-name">Brightwell<br>Painting</div>
    </div>
    <div class="divider"></div>
    <div class="contact">
      <div class="person-name">Daniel Harlow</div>
      <div class="person-role">Director</div>
      <div class="address">418 Linden Avenue #3<br>Oakridge, WI 53027</div>
      <div class="contact-line">
        <svg viewBox="0 0 12 12"><path d="M3 1 L5 3.5 L4 4.8 Q5 7 7.2 8 L8.5 7 L11 9 L9.8 11 Q4 10.5 1 3 Z" fill="#2b2b2b"/></svg>
        <span>262-555-0147</span>
      </div>
      <div class="contact-line">
        <svg viewBox="0 0 12 12"><rect x="1" y="2.5" width="10" height="7" fill="none" stroke="#2b2b2b" stroke-width="1.2"/><path d="M1 2.5 L6 6.5 L11 2.5" fill="none" stroke="#2b2b2b" stroke-width="1.2"/></svg>
        <span>brightwelloffice@mail.com</span>
      </div>
      <div class="contact-line">
        <svg viewBox="0 0 12 12"><circle cx="6" cy="6" r="5" fill="none" stroke="#2b2b2b" stroke-width="1.1"/><ellipse cx="6" cy="6" rx="2.2" ry="5" fill="none" stroke="#2b2b2b" stroke-width="1"/><path d="M1 6 H11" stroke="#2b2b2b" stroke-width="1"/></svg>
        <span>www.brightwellpainting.com</span>
      </div>
    </div>
  </section>

  <section class="card card-back">
    <div class="back-brand">
      <span class="back-mark"></span>
      <span>Brightwell Painting</span>
    </div>
  </section>
</main>
</body>
</html>
```